A flyer for future customers to get acquainted with our company

The flyer/card is intended for intermediaries. The purpose of this flyer is to introduce businesses to Dovrel.

It should convey: real estate and financing, with actual images. Various keywords describing what we do: project financing, temporary real estate financing, real estate financing, investment properties, transformations. We distinguish ourselves by being fast, flexible, and personal.

Please ensure the front has an attractive and inviting appearance, and leave space on the back for additional text.

Color codes: #E85B35 en #091E33

```html
<!DOCTYPE html>
<html lang="en">
<head>
<meta charset="utf-8">
<title>Dovrel – Real Estate and Financing Postcard</title>
<link rel="stylesheet" href="https://fonts.googleapis.com/css2?family=Montserrat:wght@400;600;800&family=Oswald:wght@500;600&display=swap">
<style>
  :root {
    --orange: #E85B35;
    --navy: #091E33;
    --ink: #111111;
    --paper: #ffffff;
    --rule: #555555;
  }
  html, body {
    margin: 0;
    padding: 0;
    width: 1199px;
    height: 1200px;
    overflow: hidden;
    background: var(--paper);
  }
  .canvas {
    position: relative;
    width: 1199px;
    height: 1200px;
  }
  .card {
    position: absolute;
    top: 227px;
    width: 528px;
    height: 747px;
    background: var(--paper);
    box-shadow: 0 6px 18px rgba(0,0,0,0.18);
  }
  .card--front { left: 54px; }
  .card--back { left: 619px; }
  .card svg { display: block; width: 528px; height: 747px; }

  .brand-name { font-family: "Montserrat", sans-serif; font-weight: 800; fill: var(--navy); letter-spacing: -0.5px; }
  .headline { font-family: "Oswald", sans-serif; font-weight: 600; letter-spacing: 0.4px; }
  .headline--orange { fill: var(--orange); }
  .headline--dark { fill: var(--ink); }
  .headline--light { fill: var(--paper); }
  .services { font-family: "Montserrat", sans-serif; font-weight: 400; fill: var(--paper); font-size: 10px; }
  .services__promise { font-weight: 600; fill: var(--orange); }
  .contact { font-family: "Montserrat", sans-serif; font-weight: 400; fill: var(--paper); font-size: 10px; }
  .address-line { stroke: var(--rule); stroke-width: 1; }
  .stamp-box { fill: none; stroke: var(--ink); stroke-width: 1; }
</style>
</head>
<body>
<main class="canvas">

  <section class="card card--front" aria-label="Postcard front">
    <svg viewBox="0 0 423 598" xmlns="http://www.w3.org/2000/svg">
      <defs>
        <linearGradient id="meetingTones" x1="0" y1="0" x2="1" y2="1">
          <stop offset="0" stop-color="#8c8f92"/>
          <stop offset="0.45" stop-color="#5b5753"/>
          <stop offset="1" stop-color="#a7835f"/>
        </linearGradient>
        <linearGradient id="cityTones" x1="0" y1="0" x2="0" y2="1">
          <stop offset="0" stop-color="#2a3b50"/>
          <stop offset="1" stop-color="var(--navy)"/>
        </linearGradient>
      </defs>

      <rect width="423" height="598" fill="var(--paper)"/>

      <g class="hero-photo" role="img" aria-label="Photo of a business meeting with a model house and clasped hands over documents">
        <polygon points="0,0 58,0 230,120 423,92 423,323 221,323 221,175 0,175" fill="url(#meetingTones)"/>
      </g>
      <polygon class="accent-triangle" points="423,92 423,323 221,323" fill="var(--orange)" opacity="0.82"/>
      <polygon class="accent-triangle" points="423,92 423,250 330,168" fill="var(--orange)"/>

      <rect class="accent-bar" x="267" y="333" width="156" height="10" fill="var(--navy)"/>

      <text class="brand-name" x="390" y="90" font-size="42" text-anchor="end">Dovrel</text>

      <text class="headline headline--orange" x="29" y="246" font-size="31">REAL ESTATE</text>
      <text class="headline headline--dark" x="29" y="285" font-size="26">AND FINANCING</text>

      <g class="city-photo" role="img" aria-label="Dark photo of a person looking out over a city skyline">
        <polygon points="0,503 250,393 423,393 423,598 0,598" fill="url(#cityTones)"/>
      </g>
      <polygon class="accent-triangle" points="0,305 250,393 0,503" fill="var(--orange)"/>

      <text class="headline headline--light" x="29" y="423" font-size="22">WHAT WE DO:</text>

      <g class="services" text-anchor="end">
        <text x="340" y="482">Project financing, temporary</text>
        <text x="340" y="495">real estate financing, real estate financing,</text>
        <text x="340" y="508">investment properties,transformations.</text>
        <text class="services__promise" x="340" y="526">Fast, flexible and personal.</text>
      </g>

      <rect class="contact-band" x="0" y="559" width="423" height="18" fill="var(--orange)"/>
      <text class="contact" x="211.5" y="572" text-anchor="middle">0612 448 905 | hello@dovrel.com | www.dovrel.com</text>
    </svg>
  </section>

  <section class="card card--back" aria-label="Postcard back">
    <svg viewBox="0 0 423 598" xmlns="http://www.w3.org/2000/svg">
      <defs>
        <linearGradient id="cityTonesBack" x1="0" y1="0" x2="0" y2="1">
          <stop offset="0" stop-color="#2a3b50"/>
          <stop offset="1" stop-color="var(--navy)"/>
        </linearGradient>
      </defs>

      <rect width="423" height="598" fill="var(--paper)"/>

      <rect class="stamp-box" x="319.5" y="33.5" width="67" height="81"/>

      <g class="address-lines">
        <line class="address-line" x1="29" y1="162" x2="244" y2="162"/>
        <line class="address-line" x1="29" y1="197" x2="244" y2="197"/>
        <line class="address-line" x1="29" y1="232" x2="244" y2="232"/>
        <line class="address-line" x1="29" y1="267" x2="244" y2="267"/>
      </g>

      <text class="brand-name" x="386" y="405" font-size="34" text-anchor="end">Dovrel</text>

      <g class="city-photo" role="img" aria-label="Dark photo of a person looking out over a city skyline">
        <polygon points="0,560 240,430 423,478 423,598 0,598" fill="url(#cityTonesBack)"/>
      </g>
      <polygon class="accent-triangle" points="0,325 284,428 0,560" fill="var(--orange)"/>

      <text class="headline headline--light" x="29" y="428" font-size="28">REAL ESTATE</text>
      <text class="headline headline--light" x="29" y="451" font-size="21">AND FINANCING</text>

      <rect class="contact-band" x="0" y="559" width="423" height="18" fill="var(--orange)"/>
      <text class="contact" x="211.5" y="572" text-anchor="middle">0612 448 905 | hello@dovrel.com | www.dovrel.com</text>
    </svg>
  </section>

</main>
</body>
</html>
```